Menu Design Project

We are looking for a menu for our bar restaurant in amsterdam "Verbeek".

The bar is modern and has offer food and cocktails as long as drink all day.

We are looking for something very modern but classic and professional.

This is about a classic menu for food, drinks and cocktails for a bar restaurant.

Target Market(s)

all ages

Industry/Entity Type

Restaurant

Requirements
Must have
• - Classic
- Clean
- Professional
Nice to have
• - Modern Design
- Lines and abstracts shapes
- Color combination
Should not have
• - Tribals
- Florals
- Any kind of specfic shapes

```html
<!DOCTYPE html>
<html lang="en">
<head>
<meta charset="utf-8">
<title>Verbeek Restaurant &amp; Wine Bar – Menu</title>
<link rel="stylesheet" href="https://fonts.googleapis.com/css2?family=Pacifico&family=Josefin+Sans:wght@300;400&family=Cormorant+Garamond:wght@500;600&display=swap">
<style>
  :root {
    --page: #ffffff;
    --board: #2b2b2b;
    --ink: #f2f2f2;
    --teal: #1b8e9f;
    --orange: #c8692c;
    --rule: #8a8a8a;
    --disc: #e9e9e9;
    --script: "Pacifico", cursive;
    --display: "Josefin Sans", sans-serif;
    --serif: "Cormorant Garamond", serif;
  }
  * { box-sizing: border-box; margin: 0; padding: 0; }
  html, body { width: 1200px; height: 1200px; overflow: hidden; background: var(--page); }
  .canvas { position: relative; width: 1200px; height: 1200px; overflow: hidden; background: var(--page); }

  .panel { position: absolute; background: var(--board); color: var(--ink); overflow: hidden; }
  .panel-frame { position: absolute; inset: 0; width: 100%; height: 100%; }
  .centered { position: absolute; left: 0; right: 0; text-align: center; white-space: nowrap; }

  .brand-disc { position: absolute; left: 50%; border-radius: 50%; background: var(--disc); border: 4px solid var(--board); box-shadow: 0 0 0 2px var(--disc); }

  /* cover */
  .cover { left: 6px; top: 6px; width: 382px; height: 808px; }
  .season { top: 56px; font: 300 15px/1 var(--display); letter-spacing: 1px; }
  .cover .brand-disc { top: 174px; width: 112px; height: 112px; margin-left: -56px; }
  .brand-name { top: 300px; font: 400 21px/1.2 var(--script); }
  .headline { font: 300 42px/1 var(--display); letter-spacing: -1.5px; transform: scaleY(1.3); transform-origin: top center; }
  .headline-1 { top: 362px; }
  .headline-2 { top: 418px; }
  .amp { position: absolute; left: 178px; top: 398px; width: 28px; height: 28px; border-radius: 50%; background: var(--teal); color: #fff; font: 400 12px/28px var(--script); text-align: center; }
  .orange-rule { position: absolute; left: 32px; right: 32px; height: 1px; background: var(--orange); }
  .tagline-script { top: 522px; font: 400 19px/1.2 var(--script); color: var(--teal); }
  .cover-line { font: 300 19px/1.2 var(--display); }
  .dot-rule { position: absolute; left: 50px; right: 50px; border-top: 2px dotted var(--ink); }

  /* back panel */
  .info { left: 396px; top: 6px; width: 382px; height: 808px; }
  .rail { position: absolute; top: 12px; bottom: 12px; width: 1px; background: var(--ink); }
  .info .brand-disc { top: 136px; width: 100px; height: 100px; margin-left: -50px; }
  .info-name { top: 242px; font: 400 12px/1.2 var(--script); }
  .script-title { font: 400 28px/1.2 var(--script); }
  .hours { position: absolute; top: 344px; font: 600 9.5px/1.15 var(--serif); white-space: nowrap; }
  .address { top: 414px; font: 500 10px/1.2 var(--serif); }
  .phone { top: 478px; font: 500 10px/1 var(--serif); }

  /* inside spread */
  .spread { left: 547px; top: 514px; width: 599px; height: 634px; }
  .band { position: absolute; left: 0; right: 0; top: 25px; height: 44px; background: var(--teal); }
  .band::before, .band::after { content: ""; position: absolute; left: 0; right: 0; border-top: 1px dashed rgba(255,255,255,.7); }
  .band::before { top: 4px; } .band::after { bottom: 4px; }
  .band-title { position: absolute; top: 10px; font: 400 13px/1.4 var(--script); color: #fff; }
  .band-left { left: 104px; }
  .band-right { right: 22px; }
  .spread .brand-disc { left: 48px; top: 8px; width: 72px; height: 72px; margin-left: -36px; border-width: 3px; }

  .section { position: absolute; width: 258px; }
  .section-title { font: 400 14px/1.3 var(--script); padding-bottom: 3px; width: 112px; border-bottom: 1px solid var(--rule); margin-bottom: 6px; }
  .intro { font: 500 8px/1.2 var(--serif); margin-bottom: 5px; }
  .item { border-bottom: 1px dotted #666; }
  .item-head { display: flex; justify-content: space-between; font: 600 8.5px/1.15 var(--serif); font-variant: small-caps; color: var(--teal); letter-spacing: .2px; }
  .item-desc { font: 500 7.5px/1.2 var(--serif); color: var(--ink); white-space: nowrap; overflow: hidden; text-overflow: clip; }
  .item-short { padding: 3px 0; }
</style>
</head>
<body>
<div class="canvas">

  <section class="panel cover">
    <svg class="panel-frame" viewBox="0 0 382 808" aria-hidden="true">
      <g fill="none" stroke="#e6e6e6" stroke-width="1.3">
        <rect x="18" y="18" width="346" height="772"/>
        <rect x="24" y="24" width="334" height="760"/>
        <rect x="8" y="8" width="14" height="14"/><rect x="360" y="8" width="14" height="14"/>
        <rect x="8" y="786" width="14" height="14"/><rect x="360" y="786" width="14" height="14"/>
      </g>
    </svg>
    <p class="centered season">SUMMER - AUTUMN 2013</p>
    <div class="brand-disc"></div>
    <p class="centered brand-name">Verbeek</p>
    <h1 class="centered headline headline-1">RESTAURANT</h1>
    <p class="centered headline headline-2">WINE BAR</p>
    <span class="amp">&amp;</span>
    <div class="orange-rule" style="top:516px"></div>
    <p class="centered tagline-script">Verbeek Bar Restaurant</p>
    <div class="orange-rule" style="top:562px"></div>
    <p class="centered cover-line" style="top:586px">FOOD MENU &amp; COCKTAILS</p>
    <p class="centered cover-line" style="top:620px;font-size:14px">W</p>
    <div class="dot-rule" style="top:655px"></div>
    <p class="centered cover-line" style="top:670px;font-size:16px">FRESH MEAT AND FISH</p>
    <div class="dot-rule" style="top:702px"></div>
    <p class="centered cover-line" style="top:716px;font-size:16px;line-height:1.15">DELICIOUS CUISINE FROM HOLLAND<br>HOME MADE GOURMET DISHES</p>
  </section>

  <section class="panel info">
    <svg class="panel-frame" viewBox="0 0 382 808" aria-hidden="true">
      <g fill="none" stroke="#e6e6e6" stroke-width="1.3">
        <path d="M18 40V18H40M342 18H364V40M364 768V790H342M40 790H18V768"/>
        <rect x="8" y="8" width="14" height="14"/><rect x="360" y="8" width="14" height="14"/>
        <rect x="8" y="786" width="14" height="14"/><rect x="360" y="786" width="14" height="14"/>
      </g>
    </svg>
    <div class="rail" style="left:80px"></div>
    <div class="rail" style="left:305px"></div>
    <div class="brand-disc"></div>
    <p class="centered info-name">Verbeek Bar Restaurant</p>
    <h2 class="centered script-title" style="top:290px">Opening hours</h2>
    <p class="hours" style="left:100px">Monday to Friday<br>9am – 5pm</p>
    <p class="hours" style="left:184px">Saturday<br>9am – 5pm</p>
    <p class="hours" style="left:246px">Sunday<br>10am – 4pm</p>
    <h2 class="centered script-title" style="top:370px">Contact us</h2>
    <p class="centered address">Verbeek Bar Restaurant<br>Amsterdam<br>Keizersgracht 214<br>Noord-Holland<br>1017 KD</p>
    <p class="centered phone">Telephone: (020) 555 0142</p>
  </section>

  <section class="panel spread">
    <div class="band">
      <span class="band-title band-left">Food &amp; Drinks Menu</span>
      <span class="band-title band-right">- Main Dishes &amp; Starters -</span>
    </div>
    <div class="brand-disc"></div>

    <div class="section" style="left:26px;top:104px">
      <h3 class="section-title">Starters</h3>
      <div class="item"><div class="item-head"><span>Cappuccino</span><span>£1.95</span></div><p class="item-desc">A shot of espresso and frothed milk dusted with chocolate powder</p></div>
      <div class="item"><div class="item-head"><span>Latte (white coffee)</span><span>£1.95</span></div><p class="item-desc">A shot of espresso topped up with hot milk</p></div>
      <div class="item"><div class="item-head"><span>Americano (black coffee)</span><span>£1.75</span></div><p class="item-desc">A shot of espresso topped up with hot water</p></div>
      <div class="item"><div class="item-head"><span>Chocolate</span><span>£1.85</span></div><p class="item-desc">Smooth and rich hot chocolate with a milk froth</p></div>
      <div class="item"><div class="item-head"><span>Espresso</span><span>£1.20</span></div><p class="item-desc">A short rich shot of gourmet coffee</p></div>
      <div class="item"><div class="item-head"><span>Decaffeinated Coffee</span><span>£1.60</span></div><p class="item-desc">A cup of decaffeinated coffee served with hot milk</p></div>
      <div class="item"><div class="item-head"><span>Vanilla Latte</span><span>£2.10</span></div><p class="item-desc">A shot of espresso topped up with hot milk with a hint of vanilla</p></div>
      <div class="item"><div class="item-head"><span>Tea</span><span>£0.95</span></div><p class="item-desc">A pot of English tea</p></div>
      <div class="item"><div class="item-head"><span>Green tea</span><span>£1.05</span></div><p class="item-desc">An individual cup of green tea</p></div>
    </div>

    <div class="section" style="left:325px;top:104px">
      <h3 class="section-title">Main Dishes</h3>
      <div class="item"><div class="item-head"><span>Tuna Mayo</span><span>£2.05</span></div><p class="item-desc">Tuna &amp; Mayonnaise with sweet corn in either a baguette or sandwich</p></div>
      <div class="item"><div class="item-head"><span>BLT</span><span>£2.05</span></div><p class="item-desc">Bacon, Lettuce and Tomato with salad in either a baguette or sandwich</p></div>
      <div class="item"><div class="item-head"><span>The Big Breakfast</span><span>£2.75</span></div><p class="item-desc">Everything you need to start the day! Sausage, scrambled egg, bacon, mushrooms.</p></div>
      <div class="item"><div class="item-head"><span>Coronation Chicken</span><span>£2.45</span></div><p class="item-desc">Simple creamy coronation chicken in either a baguette or sandwich</p></div>
      <div class="item"><div class="item-head"><span>Chilli Chicken</span><span>£2.45</span></div><p class="item-desc">Mild spicy pieces of chicken with mayo in either a baguette or sandwich</p></div>
      <div class="item"><div class="item-head"><span>Piri Piri Chicken</span><span>£2.50</span></div><p class="item-desc">Some like it HOT with our piri chicken; Mild, Medium or Hot.</p></div>
      <div class="item"><div class="item-head"><span>Bacon</span><span>£2.05</span></div><p class="item-desc">with a choice of Smoked or Un-Smoked bacon</p></div>
      <div class="item"><div class="item-head"><span>Brie, Salad &amp; Cranberry or Mango Chutney (veggie)</span><span>£2.45</span></div><p class="item-desc">A tasty brie sensation</p></div>
      <div class="item item-short"><div class="item-head"><span>Vegetable Nugget Wrap Sweet Thai Chilli (veggie)</span><span>£2.45</span></div></div>
    </div>

    <div class="section" style="left:26px;top:404px">
      <h3 class="section-title">Desserts ...</h3>
      <div class="item"><div class="item-head"><span>Orange juice</span><span>£1.10</span></div><p class="item-desc">Made with fresh oranges</p></div>
      <div class="item"><div class="item-head"><span>Apple juice</span><span>£1.10</span></div><p class="item-desc">Made with the finest apples</p></div>
      <div class="item"><div class="item-head"><span>Sparkling water</span><span>£1.00</span></div><p class="item-desc">Carbonated spring water in a choice of flavours</p></div>
      <div class="item"><div class="item-head"><span>Spring water</span><span>£1.00</span></div><p class="item-desc">Natural mineral water</p></div>
      <div class="item"><div class="item-head"><span>Cranberry juice</span><span>£1.10</span></div><p class="item-desc">Home made fresh cranberry juice</p></div>
      <div class="item"><div class="item-head"><span>Dandelion and burdock</span><span>£1.75</span></div><p class="item-desc">Botanical infusion of dandelion and burdock with ginger extract</p></div>
      <div class="item"><div class="item-head"><span>Home made lemonade</span><span>£1.50</span></div><p class="item-desc">Botanical lemon drink with ginger and herbal extracts</p></div>
      <div class="item"><div class="item-head"><span>Elderflower lemonade</span><span>£1.60</span></div><p class="item-desc">Made from fresh elderflower</p></div>
    </div>

    <div class="section" style="left:325px;top:404px">
      <h3 class="section-title">Drinks...</h3>
      <p class="intro">Why not indulge yourself with our selection of home made cakes and pastries, the perfect compliment to go with a lovely coffee.</p>
      <div class="item"><div class="item-head"><span>A slice of cake</span><span>£1.50</span></div><p class="item-desc">Served with cream</p></div>
      <div class="item"><div class="item-head"><span>Handmade scone</span><span>£1.35</span></div><p class="item-desc">Served with butter</p></div>
      <div class="item"><div class="item-head"><span>Handmade jam scone</span><span>£1.40</span></div><p class="item-desc">Served with cream</p></div>
      <div class="item item-short"><div class="item-head"><span>Muffins</span><span>£1.35</span></div></div>
      <div class="item item-short"><div class="item-head"><span>Danish pastries</span><span>£1.20</span></div></div>
      <div class="item item-short"><div class="item-head"><span>Cookies</span><span>£1.00</span></div></div>
      <div class="item item-short"><div class="item-head"><span>Flap jacks</span><span>£1.25</span></div></div>
      <div class="item item-short"><div class="item-head"><span>Carrot cake</span><span>£1.80</span></div></div>
    </div>
  </section>

</div>
</body>
</html>
```